Design Creative Banner or Gif Ads. 3 Designs To Be Selected

Come up with some creative banner ads for stonewell.co.nz

*At least 3 different winning banners will be chosen*

Please provide banner ads / gif ads in common google ads / website banner formats.

They can be gif or static but must stand out while still maintaining clear clean text and visuals, with a premium professional feel (please avoid clip art or anything that gives a cheap message).

Please keep in mind that these will likely be small ads so text needs to be large and if there's there a lot of text then use multiple frames/ pages as submit as a gif.

Style
Minimal & clean lines
Architectural or realistic images
Avoid cartoon styles, clipart, or anything that looks cheap

Font
Nexa or Montserrat or similar

Tone
Premium, serious, trustworthy — fits new builds

Colours
Option 1: Deep Navy (trust & quality) & lighter blues and warm grey
Option 2: Open to bright colours to help the ads stand out, such as (but not limited to) bright pink with black, yellow, fluorescent green, provided the messaging is still done professionally.
Our logo is attached (Stone Well Logo)

Display Sizes
Ad specs for file sizes should be file formats like JPEG, GIF, and PNG, with animations limited to a max of 30 seconds or less.
We will need several different ad sizes provided for each of the 3 selected winning designs.

• Medium Rectangle: 300 × 250 pixels
• Leaderboard: 728 × 90 pixels
• Desktop Banner ad image: (640x360 pixels)
• Desktop Banner ad image 2: (300x600 pixels)
• Possibly one or two other sizes

Flexibility to be creative
The ad text, words, upper/lower case, layout, colour, theme, and images can be adjusted to how you think it will look best. The follow example ads are just examples of what we are after but we are keen to see what you can create.

Recommendations at this point:
1. Avoid text heavy
2. Looking for more Gif ads
3. Imaging: if possible use real stock photo's rather than AI

Themes:

1
Building Soon? Start Here
Free Build Planning Pack:
✓ Build Cost Calculator
✓ Hidden Cost Checklist
✓ Builder Comparison Guide
Build With Confidence
Download Free

2
Before You Choose A Builder
Compare Price, Scope, Risk & Value
Avoid Costly Mistakes
Choose The Right Builder With Confidence
Download The Free Guide

3
Planning A New Build?
Avoid These Common Mistakes:
✗ Hidden Exclusions
✗ Missing Scope
✗ Unrealistic Allowances
✗ Budget Blowouts
Download The Free Guide

4
Before You Buy Land
Know what it could cost to build.
Avoid Costly Building Mistakes
Download Our Free Guides

5
Know Your Build Budget?
• Free Build Cost Calculator
• Hidden Cost Checklist
• Build Planning Tools
Calculate Costs (Download)

Target Market(s)

Landowners looking to build

Industry/Entity Type

Building

Font styles to use
Other font styles liked:
• Nexa or Montserrat or similar

Requirements
Should not have
• Avoid cartoon styles, clipart, or anything that looks cheap

```html
<!DOCTYPE html>
<html lang="en">
<head>
<meta charset="utf-8">
<title>Stone Well – Know Your Build Budget</title>
<link rel="stylesheet" href="https://fonts.googleapis.com/css2?family=Montserrat:wght@400;500;600;700&display=swap">
<style>
  :root {
    --navy: #14324a;
    --navy-deep: #0d2a3f;
    --steel: #4f86a6;
    --sky: #7fc0dc;
    --muted-blue: #6f9dbb;
    --warm-grey: #5a5a5a;
    --paper: #ffffff;
    --paper-shade: #eeeeee;
  }
  * { box-sizing: border-box; margin: 0; padding: 0; }
  html, body { width: 1200px; height: 2400px; overflow: hidden; background: var(--paper); }
  .banner {
    position: relative;
    width: 1200px;
    height: 2400px;
    overflow: hidden;
    background: linear-gradient(90deg, var(--paper-shade) 0%, var(--paper) 45%, #f7f7f7 100%);
    font-family: "Montserrat", sans-serif;
    color: var(--navy);
  }
  .side-wave { position: absolute; left: 0; top: 0; width: 220px; height: 2400px; }

  .brand {
    position: absolute; left: 210px; top: 150px;
    display: flex; align-items: center; gap: 34px;
  }
  .brand-square { width: 150px; height: 150px; background: var(--navy); }
  .brand-text { display: flex; flex-direction: column; }
  .brand-name { font-size: 96px; font-weight: 600; line-height: 1; color: var(--navy); letter-spacing: -1px; }
  .brand-tagline { margin-top: 18px; font-size: 25px; font-weight: 700; color: var(--muted-blue); letter-spacing: 0.5px; }

  .rule { position: absolute; height: 10px; background: linear-gradient(90deg, var(--steel), var(--sky) 55%, var(--steel)); }
  .rule-a { left: 305px; width: 835px; top: 424px; }
  .rule-b { left: 145px; width: 855px; top: 452px; }
  .rule-c { left: 280px; width: 860px; top: 1030px; }
  .rule-d { left: 145px; width: 835px; top: 1056px; }

  .headline {
    position: absolute; left: 150px; right: 40px; top: 630px;
    text-align: center; font-size: 110px; font-weight: 700; line-height: 1.12;
    color: var(--navy);
  }
  .headline .mark { color: var(--warm-grey); }

  .perks { position: absolute; left: 185px; top: 1205px; list-style: none; }
  .perk { display: flex; align-items: flex-start; margin-bottom: 72px; }
  .perk-icon { width: 120px; height: 110px; margin-top: 22px; flex: none; }
  .perk-text { margin-left: 22px; font-size: 90px; font-weight: 600; line-height: 1.03; color: var(--navy); }

  .cta-lead {
    position: absolute; left: 300px; width: 600px; top: 2098px;
    text-align: center; font-size: 54px; font-weight: 400; color: var(--navy);
  }
  .cta-button {
    position: absolute; left: 317px; top: 2181px; width: 570px; height: 115px;
    border-radius: 12px;
    background: linear-gradient(180deg, #2a4a62 0%, var(--navy-deep) 45%, #0a2234 100%);
    box-shadow: 0 4px 8px rgba(0,0,0,0.25);
    display: flex; align-items: center; justify-content: center;
    color: var(--paper); font-size: 58px; font-weight: 500; letter-spacing: 2px;
  }
</style>
</head>
<body>
<main class="banner">
  <svg class="side-wave" viewBox="0 0 220 2400" aria-hidden="true">
    <defs>
      <linearGradient id="waveBlue" x1="0" y1="0" x2="0" y2="1">
        <stop offset="0" stop-color="#3e7393"/>
        <stop offset="0.45" stop-color="#62a8c6"/>
        <stop offset="1" stop-color="#3f6f8c"/>
      </linearGradient>
    </defs>
    <path d="M0 0 H70 C40 500 200 900 170 1400 C150 1800 110 2100 100 2400 H0 Z" fill="#c9c9c9"/>
    <path d="M0 0 H45 C15 500 170 900 140 1400 C120 1800 85 2100 75 2400 H0 Z" fill="url(#waveBlue)"/>
  </svg>

  <header class="brand">
    <div class="brand-square"></div>
    <div class="brand-text">
      <span class="brand-name">Stone Well</span>
      <span class="brand-tagline">COMPARE QUOTES FROM TRUSTED BUILDERS</span>
    </div>
  </header>

  <div class="rule rule-a"></div>
  <div class="rule rule-b"></div>

  <h1 class="headline">KNOW YOUR<br>BUILD BUDGET<span class="mark">?</span></h1>

  <div class="rule rule-c"></div>
  <div class="rule rule-d"></div>

  <svg width="0" height="0" aria-hidden="true" style="position:absolute">
    <defs>
      <linearGradient id="arrowBlue" x1="0" y1="0" x2="1" y2="1">
        <stop offset="0" stop-color="#a9d6ea"/>
        <stop offset="1" stop-color="#4f8fb0"/>
      </linearGradient>
      <symbol id="curved-arrow" viewBox="0 0 120 110">
        <path d="M18 105 C8 60 35 28 80 26 L80 6 L116 40 L80 72 L80 52 C50 52 28 72 34 105 Z" fill="url(#arrowBlue)"/>
      </symbol>
    </defs>
  </svg>

  <ul class="perks">
    <li class="perk"><svg class="perk-icon"><use href="#curved-arrow"/></svg><span class="perk-text">Free Build Cost<br>Calculator</span></li>
    <li class="perk"><svg class="perk-icon"><use href="#curved-arrow"/></svg><span class="perk-text">Hidden Cost<br>Checklist</span></li>
    <li class="perk"><svg class="perk-icon"><use href="#curved-arrow"/></svg><span class="perk-text">Build Planning<br>Tools</span></li>
  </ul>

  <p class="cta-lead">Calculate Costs</p>
  <div class="cta-button">DOWNLOAD</div>
</main>
</body>
</html>
```